Tranvik Leasing Corp - Business Card Design

Need a new modern designed business card that is different and stands out to represent my equipment financing company. Tranvik Leasing Corp finances all types of equipment and all types of industries. We like to do equipment financing a different way by putting customers first and want our card to represent that different approach to business. I want a card that some remembers when they receive it so it sticks in their mind and makes that wow impression.

Card should have a black background so the logo stands out. It can be horizontial or vertical or a combination of both.

Front of card information is below that shows the information that would go on my card. That is where I want a different look or design to stand out. The front could be split black/orange colour so the logo could pop on black side and information on orange side with different lettering. Just outside the box thinking on the front of the card. Open to any type of design.

Back of card is below which i I like unless you have a different spin to provide or a different idea that would make the card better as I am open to anything that looks great.

Target Market(s)

Tranvik Leasing Corp deals with business owners in all industries.

Industry/Entity Type

Business

Contact Information for Business Card

Colors

Designer to choose colors to be used in the design.

Requirements
Must have
• Modern
• Different
• Stand Out
• Makes an Impression

```html
<!DOCTYPE html>
<html lang="en">
<head>
<meta charset="utf-8">
<title>Tranvik Leasing Corp – Business Card</title>
<link href="https://fonts.googleapis.com/css2?family=Lato:wght@400;700&display=swap" rel="stylesheet">
<style>
  :root {
    --backdrop: #3b3b3d;
    --card: #000000;
    --orange: #f58220;
    --red: #e8262f;
    --white: #ffffff;
    --band-text: #1a0d05;
  }
  * { margin: 0; padding: 0; box-sizing: border-box; }
  html, body {
    width: 1189px;
    height: 1200px;
    overflow: hidden;
    background: var(--backdrop);
    font-family: "Lato", Arial, sans-serif;
  }
  .card {
    position: absolute;
    left: 166px;
    width: 856px;
    height: 488px;
    background: var(--card);
    overflow: hidden;
  }
  .card--back { top: 76px; border-radius: 40px 0 40px 0; }
  .card--front { top: 635px; border-radius: 0 40px 0 40px; }

  .web-band {
    position: absolute;
    left: 0;
    top: 419px;
    width: 100%;
    height: 42px;
    background: linear-gradient(180deg, var(--orange) 0%, #f36a22 55%, var(--red) 100%);
    display: flex;
    align-items: center;
    justify-content: center;
  }
  .card--back .web-band { border-radius: 0 0 28px 0; }
  .card--front .web-band { border-radius: 0 0 0 28px; }
  .web-band__url {
    color: var(--band-text);
    font-size: 20px;
    letter-spacing: 2.6px;
  }

  .brand-mark {
    position: absolute;
    display: flex;
    align-items: center;
    gap: 14px;
    color: var(--orange);
    font-weight: 400;
    white-space: nowrap;
  }
  .brand-mark__dot {
    flex: none;
    border-radius: 50%;
    background: var(--orange);
  }
  .card--back .brand-mark {
    left: 50%;
    top: 196px;
    transform: translateX(-50%);
    font-size: 40px;
  }
  .card--back .brand-mark__dot { width: 30px; height: 30px; }

  .card--front .brand-mark {
    left: 60px;
    top: 190px;
    font-size: 26px;
  }
  .card--front .brand-mark__dot { width: 20px; height: 20px; }

  .contact-name {
    position: absolute;
    left: 456px;
    top: 112px;
    color: var(--white);
    font-size: 30px;
    font-weight: 700;
    line-height: 1;
  }
  .contact-title {
    position: absolute;
    left: 457px;
    top: 150px;
    color: var(--white);
    font-size: 23px;
    line-height: 1;
  }
  .contact-details {
    position: absolute;
    left: 458px;
    top: 290px;
    color: var(--white);
    font-size: 22px;
    line-height: 29px;
  }
</style>
</head>
<body>
  <section class="card card--back" aria-label="Card back">
    <div class="brand-mark">
      <span class="brand-mark__dot"></span>
      <span class="brand-mark__name">Tranvik Leasing Corp</span>
    </div>
    <div class="web-band"><span class="web-band__url">www.tranvikleasing.ca</span></div>
  </section>

  <section class="card card--front" aria-label="Card front">
    <div class="brand-mark">
      <span class="brand-mark__dot"></span>
      <span class="brand-mark__name">Tranvik Leasing Corp</span>
    </div>
    <p class="contact-name">MARA DELCOURT</p>
    <p class="contact-title">PRESIDENT</p>
    <p class="contact-details">403.555.0182<br>mara@tranvikleasing.ca</p>
    <div class="web-band"><span class="web-band__url">www.tranvikleasing.ca</span></div>
  </section>
</body>
</html>
```